Business Card Design Project : Tidewell Press

In preparation for market launch, Whistler's Tidewell Press require the development of a business card. Tidewell Press is a Community online publishing web portal. We provide the the city of Whistler located in B.C. (Canada) business directories, News, Classified ads, News, Events and blogs etc.

The main focus of the brand is to help local businesses to corporate with their online advertisement and marketing. Meeting our clients face to face is a must (B2B).

Target Market(s)

The target market is B2B customers. Business Owners to Marketing, advertising Managers

Industry/Entity Type

Business

Requirements
Must have
• - The business card will be two sided.
the BACK side will have our logo which consist of (icon, url,slogan) submited. The logo will be middle and centred.

The FRONT side should have company details:

Company Legal Name: FERNDALE TIDEWELL PRESS

Owen Marsk
Director of Sales & Marketing

www.ferndaletidewell.biz
owen@ferndaletidewell.biz

Phone: 555 014 3826
#2817 - 562 E. Harlow Ave.
Vancouver, B.C. K7P2R4 Canada
Nice to have
• - For the "FRONT" side of our business card. You can separate or re-arrange with our logo components (icon, logo,slogan). It does not have to be together.

Also our company legal name is rather long so arrange or organize the name in a way to make it shorter. Your experience and creativity will have to come in play.
Should not have
• should not have other colors beside logo color and black text (2 colors). Also nothing Three dimensional

```html
<!DOCTYPE html>
<html lang="en">
<head>
<meta charset="utf-8">
<title>Tidewell Press – Business Card</title>
<link rel="stylesheet" href="https://fonts.googleapis.com/css2?family=Open+Sans:wght@400;600;700&display=swap">
<style>
  :root {
    --brand-blue: #2a7fc7;
    --brand-blue-light: #5a9fd8;
    --ink: #1a1a1a;
    --ink-soft: #4a4a4a;
    --card: #ffffff;
    --backdrop: #5b3b22;
  }
  * { box-sizing: border-box; margin: 0; padding: 0; }
  html, body {
    width: 1200px; height: 412px; overflow: hidden;
    background: var(--backdrop);
    font-family: "Open Sans", Arial, sans-serif;
  }
  .canvas { position: relative; width: 1200px; height: 412px; }
  .card {
    position: absolute; top: 64px;
    width: 498px; height: 285px;
    background: var(--card);
    overflow: hidden;
  }
  .card--front { left: 74px; }
  .card--back { left: 629px; }

  /* Front: brand block */
  .brand-block {
    position: absolute; left: 14px; top: 74px; width: 250px;
    text-align: center;
  }
  .brand-name {
    color: var(--brand-blue); font-weight: 700; font-size: 26px;
    line-height: 1; letter-spacing: 0.2px;
  }
  .brand-url {
    margin-top: 26px; color: var(--ink); font-weight: 700;
    font-size: 19px; line-height: 1; letter-spacing: -0.2px;
  }
  .brand-slogan {
    margin-top: 3px; color: var(--brand-blue); font-size: 14.5px; line-height: 1.1;
  }

  .divider {
    position: absolute; left: 268px; top: 68px; width: 1px; height: 118px;
    background: var(--ink-soft);
  }
  .details {
    position: absolute; left: 278px; top: 72px;
    color: var(--ink-soft); font-size: 12px; line-height: 1.45;
  }
  .company {
    font-weight: 700; font-size: 11.5px; letter-spacing: 1.4px;
    color: #555; margin-bottom: 12px;
  }
  .contact-line { display: flex; align-items: center; gap: 4px; }
  .contact-line svg { width: 10px; height: 10px; fill: var(--ink-soft); }
  .address { margin-top: 16px; }

  .footer-band {
    position: absolute; left: 0; right: 0; bottom: 0; height: 68px;
    background: linear-gradient(180deg, var(--brand-blue-light) 0%, var(--brand-blue) 45%);
  }
  .signature {
    position: absolute; right: 12px; bottom: 9px; text-align: right; color: #fff;
  }
  .person-name { font-weight: 700; font-size: 15px; line-height: 1.3; }
  .person-title { font-size: 12px; line-height: 1.3; }

  /* Back */
  .back-logo {
    position: absolute; left: 0; right: 0; top: 82px; text-align: center;
  }
  .back-logo .brand-name { font-size: 44px; }
  .back-logo .brand-url { margin-top: 40px; font-size: 30px; letter-spacing: -0.4px; }
  .back-logo .brand-slogan { margin-top: 4px; font-size: 21px; }
</style>
</head>
<body>
<main class="canvas">
  <section class="card card--front" aria-label="Card front">
    <div class="brand-block">
      <div class="brand-name">Tidewell Press</div>
      <div class="brand-url">www.ferndaletidewell.biz</div>
      <div class="brand-slogan">Your information gateway</div>
    </div>
    <div class="divider"></div>
    <div class="details">
      <div class="company">FERNDALE TIDEWELL PRESS</div>
      <div class="contact-line">
        <svg viewBox="0 0 10 10" aria-hidden="true"><path d="M2 0.5 L3.6 2.6 L2.7 3.6 C3.3 5 4.9 6.7 6.4 7.3 L7.4 6.4 L9.5 8 L8.3 9.5 C4.5 9.2 0.8 5.5 0.5 1.7 Z"/></svg>
        <span>555 014 3826</span>
      </div>
      <div class="contact-line">
        <svg viewBox="0 0 10 10" aria-hidden="true"><path d="M0.5 2.5 H9.5 V8.5 H0.5 Z M1.2 3 L5 5.8 L8.8 3 Z" fill-rule="evenodd"/></svg>
        <span>owen@ferndaletidewell.biz</span>
      </div>
      <div class="address">#2817 - 562 E. Harlow Ave.<br>Vancouver, B.C. K7P2R4 Canada</div>
    </div>
    <div class="footer-band" role="img" aria-label="Decorative blue wave band along the card foot"></div>
    <div class="signature">
      <div class="person-name">Owen Marsk</div>
      <div class="person-title">Director of Sales &amp; Marketing</div>
    </div>
  </section>

  <section class="card card--back" aria-label="Card back">
    <div class="back-logo">
      <div class="brand-name">Tidewell Press</div>
      <div class="brand-url">www.ferndaletidewell.biz</div>
      <div class="brand-slogan">Your information gateway</div>
    </div>
  </section>
</main>
</body>
</html>
```